Resort Room Letter to go in Welcome Basket

It needs the Resort Logo and a snazzier font. Probably some kind of background. It will be in full color. Dimensions 5.5in x 8in. This is the in room letter that goes with the welcome basket.

Text:

Welcome to The Resort! We have prepared this convenient Starter Pack to enhance your stay in our Luxury Condominiums. To further enhance your stay housekeeping will provide daily limited service which includes fresh towels and trash removal. Additional housekeeping services can be scheduled with the front desk for a nominal fee. Please leave the basket so that we can prepare a Starter Pack for the next guest. When you are ready to checkout simply dial **61.

Helpful Hints:

Turn the lever in the freezer to start making ice
The Waterpark can be accessed from the 1st Floor
The Indoor Waterpark is open from 9AM to 11PM
Vending with Snacks & Drinks are available on Floors 1, 2, 4, & 5
The closest grocery store is Brindle Mart
You can also conveniently order groceries via Pantrydash from Halvey's, Grove Basket, & Tandro
Additional convenience items are available for purchase at the Front Desk
Use our Express Checkout by Dialing **61

Thank you so much for choosing the Resort for your Smoky Mountain Vacation!

The Resort Management Team

```html
<!DOCTYPE html>
<html lang="en">
<head>
<meta charset="utf-8">
<title>Welcome Letter – The Resort at Laurel Ridge</title>
<link rel="stylesheet" href="https://fonts.googleapis.com/css2?family=Arimo:ital,wght@0,400;0,700;1,700&family=Great+Vibes&family=Libre+Baskerville:wght@700&display=swap">
<style>
  :root {
    --page-bg: #ebe8e3;
    --teal-deep: #4f7a83;
    --teal-soft: #7399a1;
    --cream: #fdf8ea;
    --sand: #f5e6cd;
    --gold: #d49b58;
    --gold-light: #f2d06c;
    --ink: #5d6466;
    --white: #ffffff;
  }
  * { margin: 0; padding: 0; box-sizing: border-box; }
  html, body { width: 1200px; height: 1200px; overflow: hidden; background: var(--page-bg); }
  .letter {
    position: absolute; left: 215px; top: 41px;
    width: 770px; height: 1118px;
    font-family: "Arimo", Arial, sans-serif;
    color: var(--ink);
  }
  .letter-backdrop { position: absolute; inset: 0; width: 100%; height: 100%; }
  .brand {
    position: absolute; left: 0; right: 0; top: 118px;
    text-align: center; color: var(--cream);
    font-family: "Arimo", Arial, sans-serif; font-weight: 700;
    font-size: 30px; line-height: 1.2; letter-spacing: 1px;
  }
  .welcome-title {
    position: absolute; left: 0; right: 0; top: 282px;
    text-align: center; color: var(--gold);
    font-family: "Great Vibes", cursive; font-weight: 400;
    font-size: 66px; line-height: 80px;
  }
  .intro {
    position: absolute; left: 0; right: 0; top: 370px;
    text-align: center; font-style: italic; font-weight: 700;
    font-size: 17.5px; line-height: 24px;
  }
  .details {
    position: absolute; left: 0; right: 0; top: 434px;
    text-align: center; font-size: 18px; line-height: 24.5px;
  }
  .details strong { font-weight: 700; }
  .hints-title {
    position: absolute; left: 0; right: 0; top: 744px;
    text-align: center; color: var(--gold-light);
    font-size: 20px; line-height: 24px;
  }
  .hints {
    position: absolute; left: 0; right: 0; top: 794px;
    list-style: none; text-align: center; color: var(--white);
    font-size: 17.5px; line-height: 23.5px;
  }
  .hints li::before { content: "\2666"; color: var(--gold-light); }
  .closing {
    position: absolute; left: 31px; right: 31px; top: 1018px; height: 71px;
    display: flex; align-items: center; justify-content: center;
    text-align: center; text-transform: uppercase; color: var(--cream);
    font-family: "Libre Baskerville", Georgia, serif; font-weight: 700;
    font-size: 19px; line-height: 28px;
  }
</style>
</head>
<body>
<main class="letter">
  <svg class="letter-backdrop" viewBox="0 0 950 1380" preserveAspectRatio="none" aria-hidden="true">
    <rect class="frame" x="0" y="0" width="950" height="1380" fill="var(--teal-deep)"/>
    <rect class="paper" x="22" y="18" width="906" height="1344" fill="var(--cream)"/>
    <polygon class="center-diamond" points="475,230 928,670 475,1110 22,670" fill="var(--sand)"/>
    <polygon class="top-wedge" points="22,18 928,18 475,352" fill="var(--teal-soft)"/>
    <polyline class="top-rule" points="14,18 475,356 936,18" fill="none" stroke="var(--gold)" stroke-width="5"/>
    <polygon class="bottom-wedge" points="475,776 950,1096 950,1380 0,1380 0,1096" fill="var(--teal-deep)"/>
    <polyline class="bottom-rule" points="0,1092 475,772 950,1092" fill="none" stroke="var(--gold)" stroke-width="5"/>
    <polygon class="base-band" points="0,1168 22,1158 22,1352 928,1352 928,1158 950,1168 950,1380 0,1380" fill="var(--gold)"/>
    <rect class="closing-panel" x="38" y="1256" width="874" height="84" fill="var(--gold)" stroke="var(--gold-light)" stroke-width="3"/>
  </svg>

  <div class="brand">The Resort<br>at Laurel Ridge</div>

  <h1 class="welcome-title">Welcome to The Resort!</h1>

  <p class="intro">We have prepared this convenient Starter Pack<br>to enhance your stay in our Luxury Condominiums.</p>

  <p class="details">To further enhance your stay housekeeping will provide<br>daily limited service which includes fresh towels &amp; trash removal.<br>Additional housekeeping services can be scheduled<br>with the front desk for a nominal fee.<br>Please leave the basket so that we can prepare<br>a Starter Pack for the next guest.<br>When you are ready to checkout simply dial <strong>**61.</strong></p>

  <h2 class="hints-title">Helpful Hints:</h2>
  <ul class="hints">
    <li>Turn the lever in the freezer to start making ice</li>
    <li>The Waterpark can be accessed from the 1st Floor</li>
    <li>The Indoor Waterpark is open from 9AM to 11PM</li>
    <li>Vending with Snacks &amp; Drinks are available on Floors 1, 2, 4, &amp; 5</li>
    <li>The closest grocery store is Brindle Mart</li>
    <li>You can also conveniently order groceries via Pantrydash from<br>Halvey's, Grove Basket, &amp; Tandro</li>
    <li>Additional convenience items are available for purchase at the Front Desk</li>
    <li>Use our Express Checkout by Dialing **61</li>
  </ul>

  <p class="closing">Thank you so much for choosing the Resort<br>for your Smoky Mountain Vacation!</p>
</main>
</body>
</html>
```